Premium Fitness Meal Plan Design for VoltaKor (Brand Like PlumQuarry!)

VoltaKor 6 Week Autumn Forge Meal Plan Design (Branded Handout)

πŸ“„ Overview:
We are looking for a professionally designed, branded meal plan handout for our fitness facility, VoltaKor. This meal plan will be used during our upcoming 6 Week Autumn Forge Quest, where members aim to lose body fat, build lean muscle, and improve their energy through nutrition and strength training.

The design should be highly polished, visually engaging, and reflect our brand quality β€” something on par with what you would see from larger national gym chains (e.g., Plum Quarry, K62, Delmar’s Drillyard). This is not just a text document β€” we want it to feel premium, motivating, and easy to follow, ideally something members are excited to reference and share.

🧾 Format & Layout:
Size: Standard 8.5x11 inch format (single or double-sided)

Final Output: Print-ready PDF + editable source files

Orientation: Portrait

Can be designed as either:

One visually organized front-and-back sheet

Or two clean, digestible pages presented as a mini-handout

🎨 Design Style:
Clean, energetic, and transformation-focused

Use brand colors and fonts that feel bold, fresh, and motivating

Include icons, dividers, or visual cues to separate sections (not just blocks of text)

Sections should feel approachable and empowering, not clinical or restrictive

Include room for the VoltaKor logo (provided) at the top and/or footer

πŸ“˜ Content to Include:
The following content should be visually structured and formatted in clear, engaging blocks. We’ll provide this content in a PDF format

1. Header Title:
"VoltaKor 6 Week Autumn Forge Nutrition Blueprint"

2. Introduction (Small Block):
Short blurb about the challenge goals (lose body fat, gain energy, preserve lean muscle mass)

3. Elimination List (Foods to Avoid):
A visually separated section with a list of foods and drinks that should be eliminated or greatly reduced for fat loss

4. Smart Swaps Table:
A side-by-side "Craving vs Swap" table that shows easy alternatives to popular bad habits (e.g., soda β†’ sparkling water)

5. Build-Your-Own Meal Plan Sections:
Organize these into clear categories:

Proteins

Carbs

Fats

Veggies

Extras / Smart Swaps
Use icons, color codes, or visual grids to organize these food lists

6. Tips Section (Optional Bonuses):
Hydration goal

Suggested number of meals

Protein shake recommendation

Meal timing tip

10-min walk after dinner tip

πŸ“¦ Files Provided:

All written content in organized text format

βœ… Deliverables:
Final design in print-ready PDF

Editable source file (AI, PSD, or InDesign preferred)

πŸ™Œ Inspiration:
Design should feel in line with the type of professional print materials used by high-end fitness studios. Clean lines, engaging fonts, and premium layout. We're not looking for clipart or gimmicky stock photos β€” we want the design to reflect the premium, results-driven experience our gym provides.

```html
<!DOCTYPE html>
<html lang="en">
<head>
<meta charset="utf-8">
<title>VoltaKor 6 Week Autumn Forge Nutrition Blueprint</title>
<link href="https://fonts.googleapis.com/css2?family=Teko:wght@500;600;700&family=Archivo:wght@400;600;800&family=Source+Sans+3:wght@400;600;700&display=swap" rel="stylesheet">
<style>
:root{
  --yellow:#f6d20e;
  --gold:#eeb20b;
  --ink:#0c0c0c;
  --text:#1c1c1c;
  --paper:#f4f4f4;
  --red:#e3232a;
  --green:#1c9a3e;
  --stage:#d9d9d9;
}
*{margin:0;padding:0;box-sizing:border-box}
html,body{width:1200px;height:799px;overflow:hidden}
body{background:var(--stage);position:relative;font-family:"Source Sans 3",Arial,sans-serif;color:var(--text)}
.page{position:absolute;top:62px;width:515px;height:667px;background:var(--paper);overflow:hidden}
.page--front{left:60px}
.page--back{left:624px}
.abs{position:absolute}

/* front header */
.front-head{left:0;top:0;width:515px;height:232px;background:var(--ink)}
.front-head__photo{left:170px;top:0;width:345px;height:232px;background:radial-gradient(ellipse at 65% 45%,#5a3b2a 0%,#3a2a22 35%,#1a1512 70%,rgba(12,12,12,0) 100%)}
.front-head__fade{left:150px;top:0;width:120px;height:232px;background:linear-gradient(90deg,var(--ink),rgba(12,12,12,0))}
.torn{left:0;width:515px}
.brand{font-family:"Teko",sans-serif;font-weight:700;line-height:1;letter-spacing:.5px}
.brand--front{left:34px;top:24px;font-size:48px;color:#fff}
.brand-tag{font-family:"Archivo",sans-serif;font-weight:800;font-size:6.4px;letter-spacing:2px;color:var(--yellow);white-space:nowrap}
.brand-tag--front{left:55px;top:76px}
.title-a{left:34px;top:108px;font-family:"Archivo",sans-serif;font-weight:800;font-size:24px;color:#fff;letter-spacing:-.2px;white-space:nowrap}
.title-b{left:33px;top:132px;font-family:"Archivo",sans-serif;font-weight:800;font-size:31px;color:var(--yellow);letter-spacing:-.2px;white-space:nowrap}
.goal{left:34px;top:172px;font-family:"Archivo",sans-serif;font-weight:400;font-size:11.6px;line-height:16px;color:#fff;text-transform:uppercase;letter-spacing:-.3px;white-space:nowrap}

/* banners */
.banner{left:35px;width:448px;height:35px;background:var(--ink);border:1.5px solid var(--yellow);border-radius:4px}
.banner__icon{left:4px;top:3px;width:27px;height:27px;border-radius:3px}
.banner__icon--no{background:var(--red)}
.banner__icon--yes{background:var(--green)}
.banner__title{font-family:"Teko",sans-serif;font-weight:600;color:var(--yellow);text-align:center;line-height:14px;font-size:14.5px;white-space:nowrap}
.banner__rule{top:8px;width:1px;height:18px;background:var(--yellow)}
.banner__text{color:#fff;font-weight:700;font-size:8.7px;line-height:11px;white-space:nowrap}

.list{list-style:none;font-size:8.8px;line-height:12.65px}
.list li{position:relative;padding-left:8px;white-space:nowrap}
.list li::before{content:"";position:absolute;left:0;top:5px;width:3px;height:3px;background:var(--gold)}
.list b{font-weight:700}
.list--light{color:#fff}
.list--light li::before{background:var(--yellow)}

.swap-table{left:50px;top:472px;border-collapse:collapse;font-size:8.8px;line-height:12.65px}
.swap-table th{text-align:left;font-weight:700;padding:0}
.swap-table td{padding:0;white-space:nowrap}
.swap-table td:first-child,.swap-table th:first-child{width:91px}
.swap-table td:first-child{font-weight:700;position:relative;padding-left:6px}
.swap-table td:first-child::before{content:"";position:absolute;left:0;top:5px;width:3px;height:3px;background:var(--gold)}

.front-foot{left:0;top:612px;width:515px;height:55px}
.url-front{left:0;top:637px;width:515px;text-align:center;font-weight:700;font-size:14.5px;color:var(--ink);letter-spacing:.2px}

/* back */
.back-head{left:0;top:0;width:515px;height:430px;background:radial-gradient(ellipse at 50% 65%,#3d2a1f 0%,#221915 45%,#121212 80%),var(--ink)}
.guide-title{left:0;top:14px;width:515px;text-align:center;font-family:"Teko",sans-serif;font-weight:600;font-size:31px;line-height:1;color:var(--yellow);white-space:nowrap}
.guide-intro{left:0;top:50px;width:515px;text-align:center;color:#fff;font-weight:700;font-size:12.6px;line-height:15.3px;white-space:nowrap}
.guide-intro em{font-style:normal;color:var(--yellow)}
.cat-icon{width:28px;height:28px;border:1.5px solid var(--yellow);border-radius:4px;background:var(--ink)}
.cat-title{font-family:"Teko",sans-serif;font-weight:600;font-size:20px;line-height:1;color:var(--yellow)}
.cat-sub{color:#fff;font-size:8.6px;line-height:10.5px;white-space:nowrap}
.cat-rule{height:1px;background:#6c6c6c}

.tip-icon{width:28px;height:28px;background:var(--yellow);border-radius:3px}
.tip-title{font-family:"Teko",sans-serif;font-weight:600;font-size:15px;line-height:14px;color:var(--gold);white-space:nowrap}
.list--tips{font-size:8.7px}
.brand--back{left:340px;top:574px;font-size:46px;color:var(--ink)}
.brand-tag--back{left:359px;top:619px;color:var(--gold)}
.url-pill{left:361px;top:631px;width:108px;height:13px;border-radius:7px;background:var(--yellow);text-align:center;font-weight:700;font-size:7.8px;line-height:13px;color:var(--ink)}
</style>
</head>
<body>

<section class="page page--front">
  <div class="abs front-head"></div>
  <div class="abs front-head__photo" role="img" aria-label="Photo of people eating fresh salad bowls with forks"></div>
  <div class="abs front-head__fade"></div>
  <svg class="abs torn" style="top:218px" width="515" height="30" viewBox="0 0 515 30" aria-hidden="true">
    <path d="M0 0H515V12L500 10L488 16L470 12L455 18L440 14L420 20L400 16L380 22L355 18L330 26L305 20L285 24L260 18L240 22L215 16L195 20L170 14L150 18L125 12L105 16L80 11L60 15L38 10L18 14L0 11Z" fill="#0c0c0c"/>
  </svg>

  <div class="abs brand brand--front">VoltaKor</div>
  <div class="abs brand-tag brand-tag--front">PERSONAL GROUP TRAINING</div>

  <h1 class="abs title-a">6 WEEK AUTUMN FORGE -</h1>
  <div class="abs title-b">NUTRITION BLUEPRINT</div>
  <p class="abs goal">Goal : drop body fat, maintain lean muscle, and boost energy -<br>without giving up real food or living in the kitchen.</p>

  <div class="abs banner" style="top:257px">
    <div class="abs banner__icon banner__icon--no">
      <svg width="27" height="27" viewBox="0 0 27 27" aria-hidden="true"><path d="M7 7L20 20M20 7L7 20" stroke="#fff" stroke-width="3.6" stroke-linecap="round"/></svg>
    </div>
    <div class="abs banner__title" style="left:36px;top:3px;width:160px">FOODS &amp; DRINKS TO ELIMINATE<br><span style="font-weight:500">(OR GREATLY REDUCE)</span></div>
    <div class="abs banner__rule" style="left:201px"></div>
    <p class="abs banner__text" style="left:207px;top:6px">These are the biggest culprits sabotaging fat loss -highly<br>palatable, calorie-dense, and metabolically disruptive:</p>
  </div>

  <ul class="abs list" style="left:50px;top:297px">
    <li><b>Sugary drinks</b> (sodas, energy drinks, sweet teas, juice blends)</li>
    <li><b>Fancy coffee drinks</b> (Frostinos, sugary creamers, flavor pumps)</li>
    <li><b>Fast food and fried foods</b> (even “grilled” items often packed with oils)</li>
    <li><b>Packaged snacks</b> (chips, cookies, granola bars, trail mix with candy)</li>
    <li><b>Baked goods</b> (donuts, muffins, pastries, bagels with cream cheese)</li>
    <li><b>Alcohol</b> (especially beer and sugary mixers)</li>
    <li><b>Processed carbs</b> (white breads, crackers, pasta)</li>
    <li><b>Cheese-heavy meals</b> (pizza, nachos, quesadillas)</li>
    <li><b>High-fat deli meats</b> (salami, pepperoni, sausage)</li>
    <li><b>Sauces and condiments loaded with sugar</b> (ketchup, BBQ sauce, honey mustard)</li>
  </ul>

  <div class="abs banner" style="top:431px;width:445px">
    <div class="abs banner__icon banner__icon--yes">
      <svg width="27" height="27" viewBox="0 0 27 27" aria-hidden="true"><path d="M6 14L11.5 19.5L21 8" fill="none" stroke="#fff" stroke-width="3.6" stroke-linecap="round" stroke-linejoin="round"/></svg>
    </div>
    <div class="abs banner__title" style="left:36px;top:3px;width:80px;font-size:15.5px">SMART SWAPS<br>FOR FAT LOSS</div>
    <div class="abs banner__rule" style="left:121px"></div>
    <p class="abs banner__text" style="left:127px;top:6px">Instead of cutting everything and feeling deprived, make these easy<br>grocery-store swaps that still satisfy cravings without killing your progress:</p>
  </div>

  <table class="abs swap-table">
    <thead><tr><th>CRAVING</th><th>TRY THIS INSTEAD</th></tr></thead>
    <tbody>
      <tr><td>Soda</td><td>Sparkling water with lime, Zentra, or plain water with fruit infusions</td></tr>
      <tr><td>Fancy Coffee</td><td>Coffee with unsweetened almond milk + stevia drops or cinnamon</td></tr>
      <tr><td>Chips</td><td>Rice cakes, roasted chickpeas, or crunchy cucumber with Chilimo</td></tr>
      <tr><td>Ice Cream</td><td>Frozen banana blended with protein powder (DIY “nice cream”)</td></tr>
      <tr><td>Candy</td><td>Berries, apples or dark chocolate squares (85%+)</td></tr>
      <tr><td>Pasta</td><td>Zucchini noodles, chickpea pasta, or cauliflower rice</td></tr>
      <tr><td>Pizza</td><td>Egg white wraps or low-carb tortillas with turkey pepperoni and light cheese</td></tr>
      <tr><td>Alcohol</td><td>Limit to 1x/week if needed</td></tr>
      <tr><td>Sandwich Bread</td><td>Elkana bread, low-carb wraps, or lettuce wraps</td></tr>
      <tr><td>Heavy Sauces</td><td>Mustard, salsa, hot sauce, coconut aminos, Greek yogurt-based dips</td></tr>
    </tbody>
  </table>

  <svg class="abs front-foot" width="515" height="55" viewBox="0 0 515 55" aria-hidden="true">
    <path d="M0 10L20 6L45 11L70 5L95 9L120 4L150 10L175 6L205 11L230 5L260 9L290 4L320 10L345 6L375 11L400 5L430 9L455 4L485 9L515 3V55H0Z" fill="#f6d20e"/>
  </svg>
  <div class="abs url-front">www.joinvoltakor.com</div>
</section>

<section class="page page--back">
  <div class="abs back-head" role="img" aria-label="Dark tabletop photo of fresh vegetables, a salad bowl and a measuring tape"></div>
  <svg class="abs torn" style="top:414px" width="515" height="34" viewBox="0 0 515 34" aria-hidden="true">
    <path d="M0 0H515V14L495 18L475 13L450 20L425 16L400 24L375 19L350 27L325 22L300 30L275 24L250 28L225 21L200 26L175 19L150 23L125 16L100 20L75 14L50 18L25 12L0 16Z" fill="#121212"/>
  </svg>

  <h2 class="abs guide-title">BUILD-YOUR-OWN MEAL PLAN GUIDE</h2>
  <p class="abs guide-intro">Use these fit-friendly food lists to mix &amp; match meals. Your job:<br>choose <em>1 protein, 1 carb</em> (if desired), and <em>1 fat</em> or <em>veggie</em> at each meal.<br>Keep it simple, keep it consistent.</p>

  <div class="abs cat-icon" style="left:38px;top:106px">
    <svg width="25" height="25" viewBox="0 0 25 25" aria-hidden="true"><ellipse cx="10" cy="11" rx="5.5" ry="6.5" fill="#fff"/><ellipse cx="15" cy="14" rx="5.5" ry="6.5" fill="#fff" stroke="#0c0c0c" stroke-width="1.2"/></svg>
  </div>
  <div class="abs cat-title" style="left:73px;top:107px">PROTEINS</div>
  <div class="abs cat-sub" style="left:73px;top:125px">choose 1 per meal/snack</div>
  <div class="abs cat-rule" style="left:38px;top:138px;width:206px"></div>
  <ul class="abs list list--light" style="left:55px;top:143px">
    <li>Chicken breast or thighs (air fried or grilled)</li>
    <li>Lean ground beef (90/10 or better)</li>
    <li>Ground turkey or turkey breast</li>
    <li>Center-cut pork chops</li>
    <li>Eggs / Egg whites</li>
    <li>Tuna (canned in water)</li>
    <li>Salmon or white fish</li>
    <li>Shrimp</li>
    <li>Greek yogurt (plain, low sugar)</li>
    <li>Cottage cheese (low-fat)</li>
    <li>Protein powder (whey or plant-based)</li>
    <li>Deli turkey (low-sodium)</li>
  </ul>

  <div class="abs cat-icon" style="left:276px;top:106px">
    <svg width="25" height="25" viewBox="0 0 25 25" aria-hidden="true"><path d="M4 12H21A8.5 8 0 0 1 4 12Z" fill="#fff"/><path d="M14 11L20 4M16 11L22 6" stroke="#fff" stroke-width="1.3"/></svg>
  </div>
  <div class="abs cat-title" style="left:311px;top:107px">CARBS</div>
  <div class="abs cat-sub" style="left:311px;top:125px">choose 1–2 servings per day, timed<br>post-workout or morning</div>
  <div class="abs cat-rule" style="left:276px;top:147px;width:204px"></div>
  <ul class="abs list list--light" style="left:293px;top:154px">
    <li>Jasmine or basmati rice (white or brown)</li>
    <li>Sweet potatoes or yams</li>
    <li>Rolled oats or steel cut oats</li>
    <li>Quinoa</li>
    <li>Elkana bread</li>
    <li>Rice cakes</li>
    <li>Berries (blueberries, raspberries, strawberries)</li>
    <li>Apples / Bananas</li>
    <li>Chickpeas or black beans (in moderation)</li>
  </ul>

  <div class="abs cat-icon" style="left:38px;top:306px">
    <svg width="25" height="25" viewBox="0 0 25 25" aria-hidden="true"><circle cx="8" cy="10" r="4" fill="#fff"/><circle cx="12.5" cy="7" r="4.5" fill="#fff"/><circle cx="17" cy="10" r="4" fill="#fff"/><path d="M10 13H15L14 21H11Z" fill="#fff"/></svg>
  </div>
  <div class="abs cat-title" style="left:73px;top:307px">VEGGIES</div>
  <div class="abs cat-sub" style="left:73px;top:325px">unlimited – fill your plate!</div>
  <div class="abs cat-rule" style="left:38px;top:340px;width:206px"></div>
  <ul class="abs list list--light" style="left:59px;top:345px">
    <li>Spinach, kale, arugula</li>
    <li>Zucchini, asparagus, bell peppers</li>
    <li>Broccoli, cauliflower, green beans</li>
    <li>Cucumber, tomatoes, shredded carrots</li>
    <li>Mixed greens or salad kits (watch the dressing)</li>
  </ul>

  <div class="abs cat-icon" style="left:275px;top:285px">
    <svg width="25" height="25" viewBox="0 0 25 25" aria-hidden="true"><path d="M12.5 4C16 4 19 10 19 15A6.5 6.5 0 0 1 6 15C6 10 9 4 12.5 4Z" fill="none" stroke="#fff" stroke-width="1.6"/><circle cx="12.5" cy="15" r="3" fill="#fff"/></svg>
  </div>
  <div class="abs cat-title" style="left:309px;top:285px">FATS</div>
  <div class="abs cat-sub" style="left:309px;top:303px">add small amounts to meals,<br>2–4 servings/day</div>
  <div class="abs cat-rule" style="left:275px;top:329px;width:204px"></div>
  <ul class="abs list list--light" style="left:297px;top:335px">
    <li>Avocado or guacamole</li>
    <li>Olive oil or avocado oil (cooking or drizzle)</li>
    <li>Nut butters (almond, peanut – natural only)</li>
    <li>Whole eggs</li>
    <li>Nuts (almonds, walnuts – portion controlled)</li>
    <li>Chia seeds or flax seeds</li>
  </ul>

  <div class="abs tip-icon" style="left:50px;top:448px">
    <svg width="28" height="28" viewBox="0 0 28 28" aria-hidden="true"><circle cx="14" cy="12" r="5.5" fill="#0c0c0c"/><rect x="11.5" y="17" width="5" height="4" fill="#0c0c0c"/><path d="M14 3V5M6 12H4M24 12H22M7.5 5.5L9 7M20.5 5.5L19 7" stroke="#0c0c0c" stroke-width="1.5"/></svg>
  </div>
  <div class="abs tip-title" style="left:85px;top:450px">BONUS TIPS FOR<br>MAXIMUM RESULTS</div>
  <ul class="abs list list--tips" style="left:85px;top:481px">
    <li><b>Drink 80–120 oz. water daily</b> — hydration is key for fat loss and muscle performance</li>
    <li><b>Eat 3–4 meals per day —</b> spaced every 3–4 hours</li>
    <li><b>Include protein in every meal</b> to stabilize blood sugar and support muscle</li>
    <li><b>Post-workout meal =</b> protein + carb, no added fats</li>
    <li><b>Up to, two protein shakes per day is allowed,</b> especially post-workout or on busy days</li>
    <li><b>Limit “treat” meals to 1 per week</b> (keep it controlled)</li>
  </ul>

  <div class="abs tip-icon" style="left:50px;top:566px">
    <svg width="28" height="28" viewBox="0 0 28 28" aria-hidden="true"><path d="M16 4L24 12L21 13L17 17L17 21L7 11L11 11L15 7Z" fill="#0c0c0c"/><path d="M12 16L5 23" stroke="#0c0c0c" stroke-width="2"/></svg>
  </div>
  <div class="abs tip-title" style="left:84px;top:567px">OPTIONAL<br>HABITS TO STACK</div>
  <ul class="abs list list--tips" style="left:85px;top:595px">
    <li><b>Weigh in once per week (same day/time)</b></li>
    <li><b>Prep 2–3 proteins and veggies on Sunday</b></li>
    <li><b>Keep a visible “YES/NO” food list on the fridge</b></li>
    <li><b>Add a short 10-min walk after dinner to boost digestion</b></li>
  </ul>

  <div class="abs brand brand--back">VoltaKor</div>
  <div class="abs brand-tag brand-tag--back">PERSONAL GROUP TRAINING</div>
  <div class="abs url-pill">www.joinvoltakor.com</div>
</section>

</body>
</html>
```